velmora crest beer

We are a small contract brewer looking to create a light beer for upscale markets in Miami Beach and vicinity. We need a logo that reflects the aura of Velmora Crest: hip, healthy, exciting, sexy, etc. The logo needed will be used on our product ( i.e. bottle ) and along with the bottle's lettering, must encompass these qualities. Like Tarnwick beer is synonymous with Jamaica, our goal is to be Miami Beach's official beer. We would like the logo and bottle to be modern in it's look, and have a distinct face with high visibility, easily recognizable sitting on a shelf.

Product name: VELMORA CREST

```html
<!DOCTYPE html>
<html lang="en">
<head>
<meta charset="utf-8">
<title>Velmora Crest Light – Can Label</title>
<link href="https://fonts.googleapis.com/css2?family=Josefin+Sans:wght@300;400&family=Dancing+Script:wght@400;700&display=swap" rel="stylesheet">
<style>
  :root {
    --band-light: #fbf3e8;
    --band-ray: #c99a68;
    --sea-deep: #28bde3;
    --sea-light: #8fe0e0;
    --foam: #bfeee6;
    --sand: #e9dcc6;
    --grass: #cfd06a;
    --text-dark: #3a3a3a;
    --logo-brown: #b5773e;
    --accent-orange: #c86a2a;
    --white: #ffffff;
  }
  * { margin: 0; padding: 0; box-sizing: border-box; }
  html, body { width: 1200px; height: 638px; overflow: hidden; background: #ffffff; }
  .label {
    position: relative;
    width: 1200px;
    height: 638px;
    overflow: hidden;
    font-family: "Josefin Sans", sans-serif;
    color: var(--text-dark);
  }
  .beach-scene {
    position: absolute;
    inset: 0;
    background: linear-gradient(150deg, var(--sea-deep) 0%, var(--sea-light) 30%, var(--foam) 45%, var(--sand) 62%, var(--sand) 85%, var(--grass) 100%);
  }
  .sunburst-band {
    position: absolute;
    left: 0;
    width: 1200px;
    background: linear-gradient(180deg, var(--band-light) 0%, var(--band-ray) 100%);
  }
  .sunburst-band--top { top: 0; height: 76px; }
  .sunburst-band--bottom {
    bottom: 0;
    height: 96px;
    background: linear-gradient(0deg, var(--band-light) 0%, var(--band-ray) 100%);
  }

  .nutrition {
    position: absolute;
    left: 62px;
    top: 104px;
    font-size: 14px;
    font-weight: 300;
    line-height: 1.36;
  }
  .nutrition .ingredients { width: 290px; margin-bottom: 22px; }
  .nutrition .facts { list-style: none; padding-left: 22px; }
  .nutrition .origin { margin-top: 16px; }
  .nutrition .brew-date { margin-top: 12px; }

  .brewery {
    position: absolute;
    left: 62px;
    top: 456px;
    font-size: 18px;
    font-weight: 300;
    font-style: normal;
    line-height: 1.3;
  }

  .brand-name {
    position: absolute;
    inset: 0;
    pointer-events: none;
    font-family: "Dancing Script", cursive;
    font-weight: 700;
    color: var(--logo-brown);
    line-height: 1;
  }
  .brand-name .word, .brand-name .variant { position: absolute; white-space: nowrap; }
  .brand-name .word--first { left: 380px; top: 95px; font-size: 128px; }
  .brand-name .word--second { left: 500px; top: 215px; font-size: 128px; }
  .brand-name .variant {
    left: 700px; top: 330px; font-size: 84px;
    font-weight: 400; color: var(--accent-orange);
  }

  .tagline {
    position: absolute;
    left: 895px;
    top: 112px;
    width: 300px;
    font-family: "Dancing Script", cursive;
    font-weight: 700;
    font-size: 29px;
    color: var(--white);
    transform: rotate(-10deg);
    line-height: 1.75;
  }
  .tagline span { display: block; }
  .tagline span:last-child { padding-left: 36px; }

  .abv {
    position: absolute;
    left: 965px;
    top: 498px;
    font-size: 16px;
    font-weight: 300;
  }
</style>
</head>
<body>
<main class="label">
  <div class="beach-scene" role="img" aria-label="Illustrated beach scene: turquoise sea with sailboats meeting sandy shore and a green dune, scattered confetti"></div>
  <div class="sunburst-band sunburst-band--top" role="img" aria-label="Decorative brown sunburst ray band"></div>
  <div class="sunburst-band sunburst-band--bottom" role="img" aria-label="Decorative brown sunburst ray band"></div>

  <section class="nutrition">
    <p class="ingredients">Ingredients : water,malted barley, brewer's yeast, flavouring.</p>
    <p>1 can of beer (356ml) contains[162]:</p>
    <ul class="facts">
      <li>Calories :53</li>
      <li>Fat(g): 0</li>
      <li>Carbohydrates(g): 12.64</li>
      <li>Fibers(g): 0</li>
      <li>Protein(g): 1.64</li>
      <li>Cholesterol(mg): 0</li>
    </ul>
    <p class="origin">State of Florida</p>
    <p class="brew-date">Brewing date :<br>10/2011</p>
  </section>

  <address class="brewery">
    Velmora Crest Brewery<br>
    Coral Anevue 112<br>
    Zip : 14B08K51
  </address>

  <h1 class="brand-name">
    <span class="word word--first">Velmora</span>
    <span class="word word--second">Crest</span>
    <span class="variant">light</span>
  </h1>

  <p class="tagline"><span>The best way</span><span>to stay refreshed!</span></p>

  <p class="abv">Alcohol : 0.3 % vol</p>
</main>
</body>
</html>
```